K & M Wheel Depot business cards

need business card for tire/car care company based in tampa, florida. we sell used and new tires, also we service vehicles, tune ups, oil chasnge, brakes and A/c we offer free towing with major vehicle repair and tire purchase. we also offer free estimates on any engine or a/c repair. also we have the lowest price in the city on used and new tires.

Contact Information for Business Card

4170 E Marigold Blvd,
Tampa, Fl 33581
Ph: 813-572-3186
KandMWheelDepot@Mailverse.com

Font styles to use
Serif
Sans Serif
Decorative

Requirements
Must have
• my logo, what we do ( used and new tires , oil change, brakes, tune ups, free towing vehicl. Also business info.
Nice to have
• an image of a towing truck, highlighting that we offer free towing. something close to what i have in one of the attached image

```html
<!DOCTYPE html>
<html lang="en">
<head>
<meta charset="utf-8">
<title>K &amp; M Wheel Depot – Business Cards</title>
<link href="https://fonts.googleapis.com/css2?family=Lato:wght@400;700;900&family=Tinos:wght@400;700&display=swap" rel="stylesheet">
<style>
  :root {
    --backdrop: #2a2a2a;
    --card-white: #ffffff;
    --card-shade: #e9e9e9;
    --free-blue: #2f2fb5;
    --free-blue-light: #6a6ae0;
    --tow-red: #d0353d;
    --tow-blue: #4a5f95;
    --navy: #1b2a4a;
    --panel-top: #1f2f4d;
    --panel-bottom: #8f9aa8;
    --service-yellow: #e2d31e;
    --ink: #1a1a1a;
    --icon-yellow: #f2d21a;
  }
  * { box-sizing: border-box; margin: 0; padding: 0; }
  html, body { width: 1200px; height: 873px; overflow: hidden; }
  body {
    background: var(--backdrop);
    position: relative;
    font-family: "Lato", sans-serif;
  }
  .card {
    position: absolute;
    top: 281px;
    width: 540px;
    height: 310px;
    border-radius: 16px;
    overflow: hidden;
    background: linear-gradient(160deg, var(--card-white) 55%, var(--card-shade));
  }
  .card--front { left: 45px; }
  .card--back { left: 615px; }

  /* Front */
  .free-corner { position: absolute; left: 0; top: 0; }
  .tow-headline {
    position: absolute;
    left: 250px; top: 28px;
    font-family: "Tinos", serif;
    font-size: 19px;
    line-height: 1.15;
    color: var(--tow-blue);
    letter-spacing: 0.5px;
  }
  .tow-headline .accent { color: var(--tow-red); }
  .truck-photo {
    position: absolute;
    left: 262px; top: 88px;
    width: 255px; height: 140px;
    border-radius: 10px;
    background: linear-gradient(100deg, #6b6b6b 0%, #c9c9c9 30%, #c8282e 55%, #a51c22 80%, #bdbdbd 100%);
  }
  .call-line {
    position: absolute;
    left: 200px; top: 255px;
    font-family: "Tinos", serif;
    font-weight: 700;
    font-size: 20px;
    color: var(--tow-red);
  }

  /* Back */
  .back-left { position: absolute; left: 0; top: 0; width: 330px; height: 100%; }
  .name-tab {
    position: absolute; left: 0; top: 24px;
    width: 8px; height: 24px; background: var(--ink);
  }
  .owner-name {
    position: absolute; left: 16px; top: 22px;
    font-size: 22px; font-weight: 700; color: var(--ink);
    font-variant: small-caps; letter-spacing: 0.5px;
  }
  .owner-title {
    position: absolute; left: 120px; top: 46px;
    font-size: 11px; color: var(--ink);
  }
  .brand {
    position: absolute; left: 40px; top: 108px;
    display: flex; align-items: center; gap: 10px;
  }
  .brand-dot { width: 18px; height: 18px; border-radius: 50%; background: var(--navy); }
  .brand-name { font-size: 27px; font-weight: 900; color: var(--navy); }
  .contact-list {
    position: absolute; left: 14px; top: 196px;
    list-style: none;
  }
  .contact-list li {
    display: flex; align-items: center; gap: 7px;
    font-size: 14px; color: var(--ink); height: 24px;
    white-space: nowrap;
  }
  .contact-icon {
    flex: none;
    width: 18px; height: 18px; border-radius: 4px; background: var(--ink);
    display: flex; align-items: center; justify-content: center;
  }
  .stripes { position: absolute; left: 330px; top: 0; }
  .services-panel {
    position: absolute; left: 362px; top: 0;
    width: 178px; height: 100%;
    background: linear-gradient(180deg, var(--panel-top), var(--panel-bottom));
    padding: 40px 0 0 16px;
  }
  .services-title {
    font-size: 17px; color: var(--service-yellow);
    display: flex; align-items: center; gap: 6px; margin-bottom: 14px;
  }
  .dot { width: 6px; height: 6px; border-radius: 50%; background: #fff; display: inline-block; }
  .services-list { list-style: none; padding-left: 22px; }
  .services-list li {
    font-size: 16px; color: var(--service-yellow); line-height: 23px;
    display: flex; align-items: center; gap: 8px;
  }
  .tires-note {
    position: absolute; left: 16px; bottom: 26px;
    font-size: 13px; color: var(--ink);
  }
</style>
</head>
<body>

<section class="card card--front" aria-label="Business card front">
  <svg class="free-corner" width="200" height="310" viewBox="0 0 200 310">
    <defs>
      <linearGradient id="freeBlue" x1="0" y1="0" x2="1" y2="1">
        <stop offset="0" stop-color="var(--free-blue-light)"/>
        <stop offset="1" stop-color="var(--free-blue)"/>
      </linearGradient>
    </defs>
    <polygon points="0,0 175,0 0,295" fill="url(#freeBlue)"/>
    <path d="M175,0 Q150,150 0,295 L20,300 Q165,160 192,8 Z" fill="#dcdcf0"/>
    <text x="0" y="0" transform="translate(80,150) rotate(-60)" text-anchor="middle"
          font-family="Lato, sans-serif" font-weight="900" font-size="54" fill="#ffffff">FREE</text>
  </svg>

  <p class="tow-headline"><span class="accent">TOWING</span> WITH MAJOR<br>REPAIR OR TIRE SERVICE</p>
  <div class="truck-photo" role="img" aria-label="Photo of a red flatbed tow truck"></div>
  <p class="call-line">Call us today, 813-572-3186</p>
</section>

<section class="card card--back" aria-label="Business card back">
  <div class="back-left">
    <span class="name-tab"></span>
    <p class="owner-name">Dale Porter</p>
    <p class="owner-title">C.E.O</p>

    <div class="brand">
      <span class="brand-dot"></span>
      <span class="brand-name">K &amp; M Wheel Depot</span>
    </div>

    <ul class="contact-list">
      <li>
        <span class="contact-icon"><svg width="10" height="12" viewBox="0 0 10 12"><rect x="1.5" y="0.5" width="7" height="11" rx="1.5" fill="none" stroke="var(--icon-yellow)" stroke-width="1.5"/></svg></span>
        813-572-3186
      </li>
      <li>
        <span class="contact-icon"><svg width="12" height="10" viewBox="0 0 12 10"><rect x="0.5" y="1" width="11" height="8" fill="var(--icon-yellow)"/><path d="M0.5,1 L6,5.5 L11.5,1" fill="none" stroke="var(--ink)" stroke-width="1"/></svg></span>
        KandMWheelDepot@Mailverse.com
      </li>
      <li>
        <span class="contact-icon"><svg width="12" height="12" viewBox="0 0 12 12"><circle cx="6" cy="6" r="5" fill="none" stroke="var(--icon-yellow)" stroke-width="1.5"/><path d="M1,6 H11 M6,1 Q9,6 6,11 Q3,6 6,1" fill="none" stroke="var(--icon-yellow)" stroke-width="1"/></svg></span>
        www.kmwheeldepot.com
      </li>
      <li>
        <span class="contact-icon"><svg width="10" height="12" viewBox="0 0 10 12"><path d="M5,11.5 C1,7 0.5,5.5 0.5,4.5 A4.5,4.5 0 0 1 9.5,4.5 C9.5,5.5 9,7 5,11.5 Z" fill="var(--icon-yellow)"/><circle cx="5" cy="4.5" r="1.6" fill="var(--ink)"/></svg></span>
        4170 E Marigold Blvd. Tampa, FL 33581
      </li>
    </ul>
  </div>

  <svg class="stripes" width="32" height="310" viewBox="0 0 32 310">
    <rect x="0" y="0" width="32" height="310" fill="#ffffff"/>
    <rect x="4" y="0" width="5" height="310" fill="var(--navy)"/>
    <rect x="14" y="0" width="5" height="310" fill="var(--navy)"/>
    <rect x="24" y="0" width="5" height="310" fill="var(--navy)"/>
  </svg>

  <div class="services-panel">
    <p class="services-title"><span class="dot"></span>OUR SERVICES<span class="dot"></span></p>
    <ul class="services-list">
      <li><span class="dot"></span>VEHICLES</li>
      <li><span class="dot"></span>TUNE UPS</li>
      <li><span class="dot"></span>OIL CHASNGE</li>
      <li><span class="dot"></span>BRAKES</li>
      <li><span class="dot"></span>A/C</li>
    </ul>
    <p class="tires-note">We sell used and new tires</p>
  </div>
</section>

</body>
</html>
```